Monthly Planner & To Do List on dry erase magnetic whiteboard

I'm after 2 x designs for magnetic whiteboards.
1. 17 x 13 inches is a monthly planner. Dates and month can be written in each month and then wiped off and re-written for the next month.
2. 6 x 4 inches - to do list however I don't want this to say To Do on it but will have lines to write on and possibly bullet points to check off.
I have attached below samples of other products (the ones I like the most are the first two - 9.19.52 and 9.20.34). I actually don't like the design of the others but just show them here as an example for layout purposes.
I want something that is modern, slick, simple yet stylish which is what my brand is representative of - smart, modern, organised. It will be printed onto a white board and I only want the print to be in black, no grey shading. I need a more modern font and don't like any of the swirly parts. Just clean and simple but slick.
I would like the size of the day squares to be as large as possible to fit writing in them and also for a section somewhere on the page for additional notes.

Requirements
Should not have
• Old style fonts, cartoon style or childish.

```html
<!DOCTYPE html>
<html lang="en">
<head>
<meta charset="utf-8">
<title>Monthly Planner 2018</title>
<link rel="stylesheet" href="https://fonts.googleapis.com/css2?family=Tenor+Sans&display=swap">
<style>
  :root {
    --ink: #000000;
    --board: #ffffff;
    --frame: #5a5a5a;
  }
  html, body {
    margin: 0;
    padding: 0;
    width: 1200px;
    height: 918px;
    overflow: hidden;
    background: var(--board);
  }
  .planner {
    display: block;
    width: 1200px;
    height: 918px;
  }
  .board-edge { fill: var(--board); stroke: var(--frame); stroke-width: 1.2; }
  .day-cell { fill: none; stroke: var(--ink); stroke-width: 0.8; }
  .panel-line { fill: none; stroke: var(--ink); stroke-width: 0.9; }
  .day-label, .year-label, .memo-label {
    font-family: "Tenor Sans", "Optima", sans-serif;
    fill: var(--ink);
  }
  .day-label { font-size: 19px; }
  .year-label { font-size: 29px; }
  .memo-label { font-size: 21px; text-decoration: underline; }
</style>
</head>
<body>
<svg class="planner" viewBox="0 0 1200 918" xmlns="http://www.w3.org/2000/svg">
  <rect class="board-edge" x="1.5" y="1.5" width="1196" height="914" rx="10"/>

  <g class="month-grid">
    <!-- row 1 -->
    <rect class="day-cell" x="28" y="17.6" width="132.3" height="176.5" rx="7"/>
    <rect class="day-cell" x="160.3" y="17.6" width="132.3" height="176.5" rx="7"/>
    <rect class="day-cell" x="292.6" y="17.6" width="132.3" height="176.5" rx="7"/>
    <rect class="day-cell" x="424.9" y="17.6" width="132.3" height="176.5" rx="7"/>
    <rect class="day-cell" x="557.2" y="17.6" width="132.3" height="176.5" rx="7"/>
    <rect class="day-cell" x="689.5" y="17.6" width="132.3" height="176.5" rx="7"/>
    <rect class="day-cell" x="821.8" y="17.6" width="132.3" height="176.5" rx="7"/>
    <!-- row 2 -->
    <rect class="day-cell" x="28" y="194.1" width="132.3" height="176.5" rx="7"/>
    <rect class="day-cell" x="160.3" y="194.1" width="132.3" height="176.5" rx="7"/>
    <rect class="day-cell" x="292.6" y="194.1" width="132.3" height="176.5" rx="7"/>
    <rect class="day-cell" x="424.9" y="194.1" width="132.3" height="176.5" rx="7"/>
    <rect class="day-cell" x="557.2" y="194.1" width="132.3" height="176.5" rx="7"/>
    <rect class="day-cell" x="689.5" y="194.1" width="132.3" height="176.5" rx="7"/>
    <rect class="day-cell" x="821.8" y="194.1" width="132.3" height="176.5" rx="7"/>
    <!-- row 3 -->
    <rect class="day-cell" x="28" y="370.6" width="132.3" height="176.5" rx="7"/>
    <rect class="day-cell" x="160.3" y="370.6" width="132.3" height="176.5" rx="7"/>
    <rect class="day-cell" x="292.6" y="370.6" width="132.3" height="176.5" rx="7"/>
    <rect class="day-cell" x="424.9" y="370.6" width="132.3" height="176.5" rx="7"/>
    <rect class="day-cell" x="557.2" y="370.6" width="132.3" height="176.5" rx="7"/>
    <rect class="day-cell" x="689.5" y="370.6" width="132.3" height="176.5" rx="7"/>
    <rect class="day-cell" x="821.8" y="370.6" width="132.3" height="176.5" rx="7"/>
    <!-- row 4 -->
    <rect class="day-cell" x="28" y="547.1" width="132.3" height="176.5" rx="7"/>
    <rect class="day-cell" x="160.3" y="547.1" width="132.3" height="176.5" rx="7"/>
    <rect class="day-cell" x="292.6" y="547.1" width="132.3" height="176.5" rx="7"/>
    <rect class="day-cell" x="424.9" y="547.1" width="132.3" height="176.5" rx="7"/>
    <rect class="day-cell" x="557.2" y="547.1" width="132.3" height="176.5" rx="7"/>
    <rect class="day-cell" x="689.5" y="547.1" width="132.3" height="176.5" rx="7"/>
    <rect class="day-cell" x="821.8" y="547.1" width="132.3" height="176.5" rx="7"/>
    <!-- row 5 -->
    <rect class="day-cell" x="28" y="723.6" width="132.3" height="176.5" rx="7"/>
    <rect class="day-cell" x="160.3" y="723.6" width="132.3" height="176.5" rx="7"/>
    <rect class="day-cell" x="292.6" y="723.6" width="132.3" height="176.5" rx="7"/>
    <rect class="day-cell" x="424.9" y="723.6" width="132.3" height="176.5" rx="7"/>
    <rect class="day-cell" x="557.2" y="723.6" width="132.3" height="176.5" rx="7"/>
    <rect class="day-cell" x="689.5" y="723.6" width="132.3" height="176.5" rx="7"/>
    <rect class="day-cell" x="821.8" y="723.6" width="132.3" height="176.5" rx="7"/>
  </g>

  <g class="weekday-labels">
    <text class="day-label" x="41" y="46">SUN</text>
    <text class="day-label" x="173" y="45">MON</text>
    <text class="day-label" x="305" y="47">TUES</text>
    <text class="day-label" x="438" y="46">WED</text>
    <text class="day-label" x="569" y="47">THU</text>
    <text class="day-label" x="703" y="46">FRI</text>
    <text class="day-label" x="833" y="47">SAT</text>
  </g>

  <g class="month-year">
    <path class="panel-line" d="M966 17.6 V44 Q966 50.4 972.4 50.4 H1188"/>
    <text class="year-label" x="1175" y="41" text-anchor="end">/ 2018</text>
  </g>

  <g class="memo-panel">
    <path class="panel-line" d="M966 900 V69 Q966 62.4 972.4 62.4 H1188"/>
    <text class="memo-label" x="1080" y="94" text-anchor="middle">Memo</text>
  </g>
</svg>
</body>
</html>
```